User help guide for software for investment bank

We need a professional design for our user help guides for new software we have written for our client. We develop visualization software for investment banks in Singapore mainly focused in the financial and risk management area. Our help guides are design to show them how the software works as well as promote our brand
Updates

Project Deadline Extended Reason: I am looking for more alternative designs and we have around 10 more documents to do after this Added Saturday, November 21, 2015

Target Market(s)

Investment banking, risk management, finance

Industry/Entity Type

Bank

Requirements
Must have
• Content of document and logos
• Colour sheme
• Professional brouchure design
• Quorvin and bimsot logos on it
• Look at www.quorvin-example.com for company looks and feel
• PLEASE USE COLOUR SCHEMES BELOW IN ATTACHMENT AND FOLLOW SIMILAR STYLE TO CLIENT ANNUAL REPORT

```html
<!DOCTYPE html>
<html lang="en">
<head>
<meta charset="utf-8">
<title>LDG Actuals Analyser – Help Guide Covers</title>
<link href="https://fonts.googleapis.com/css2?family=Arimo:wght@400&display=swap" rel="stylesheet">
<style>
  :root {
    --backdrop: #000000;
    --paper: #ffffff;
    --ink: #4a4a4a;
    --ink-soft: #6b6b6b;
    --rule: #b5b5b5;
    --brand-red: #e3001b;
    --client-blue: #0a6eb5;
    --label-blue: #1a73b8;
    --client-green: #3aa13f;
  }
  * { margin: 0; padding: 0; box-sizing: border-box; }
  html, body { width: 1200px; height: 854px; overflow: hidden; background: var(--backdrop); }
  body { font-family: "Arimo", Arial, sans-serif; color: var(--ink); position: relative; }

  .page { position: absolute; top: 6px; width: 591px; height: 836px; background: var(--paper); overflow: hidden; }
  .page--back { left: 6px; }
  .page--front { left: 603px; }

  .rule { position: absolute; height: 1px; background: var(--rule); }

  /* back cover */
  .back-title { position: absolute; left: 57px; top: 52px; font-size: 12px; color: var(--ink-soft); }
  .back-top-rule { left: 57px; top: 71px; width: 478px; }
  .brand { position: absolute; display: flex; align-items: center; }
  .brand__square { background: var(--brand-red); }
  .brand__name { color: var(--ink); letter-spacing: 0.18em; font-weight: 400; }
  .back-brand { left: 83px; top: 696px; }
  .back-brand .brand__square { width: 28px; height: 28px; margin-right: 8px; }
  .back-brand .brand__name { font-size: 30px; line-height: 28px; }
  .contact { position: absolute; left: 83px; top: 738px; font-size: 12px; color: var(--ink-soft); line-height: 18px; list-style: none; }
  .contact li { display: flex; align-items: center; }
  .contact svg { width: 10px; height: 10px; margin-right: 9px; fill: var(--ink); }
  .contact__web { padding-left: 0; }
  .back-bottom-rule { left: 56px; top: 794px; width: 479px; }

  /* front cover */
  .front-top-rule { left: 58px; top: 72px; width: 477px; }
  .doc-kicker { position: absolute; left: 58px; top: 75px; font-size: 8px; color: var(--label-blue); }
  .doc-title { position: absolute; left: 58px; top: 86px; font-size: 15px; color: var(--ink); font-weight: 400; }
  .hero { position: absolute; left: 0; top: 216px; width: 591px; height: 437px;
    background:
      radial-gradient(ellipse at 55% 60%, #8fa9d6 0%, #4b6a9c 18%, transparent 40%),
      linear-gradient(180deg, #5a6670 0%, #3a4a3e 22%, #253422 55%, #1b2419 100%); }
  .client { position: absolute; right: 55px; top: 672px; display: flex; align-items: center; }
  .client__name { font-size: 27px; line-height: 27px; color: var(--client-blue); text-align: right; margin-right: 10px; }
  .client__mark { width: 40px; height: 40px; border-radius: 50%; background: var(--client-green); }
  .product-name { position: absolute; right: 55px; top: 736px; font-size: 18px; color: var(--ink-soft); }
  .partner { position: absolute; left: 58px; top: 778px; display: flex; align-items: center; }
  .partner__square { width: 14px; height: 14px; background: var(--client-blue); margin-right: 5px; }
  .partner__name { font-size: 13px; letter-spacing: 0.2em; color: var(--ink); }
  .front-brand { right: 57px; top: 779px; }
  .front-brand .brand__square { width: 11px; height: 11px; margin-right: 3px; }
  .front-brand .brand__name { font-size: 12px; line-height: 11px; }
  .front-bottom-rule { left: 58px; top: 794px; width: 477px; }
  .page-index { position: absolute; left: 58px; top: 806px; display: flex; gap: 8px; list-style: none; }
  .page-index li { width: 10px; height: 9px; border: 1px solid var(--rule); font-size: 6px; line-height: 7px; text-align: center; color: var(--ink-soft); }
  .page-index li.wide { width: 12px; }
</style>
</head>
<body>
  <section class="page page--back">
    <p class="back-title">LDG Actuals Analyser</p>
    <div class="rule back-top-rule"></div>

    <div class="brand back-brand">
      <span class="brand__square"></span>
      <span class="brand__name">BIMSOT</span>
    </div>
    <ul class="contact">
      <li><svg viewBox="0 0 10 10"><path d="M5 0.5 L0 5 H1.5 V9.5 H4 V6.5 H6 V9.5 H8.5 V5 H10 Z"/></svg>Carrer del Vell 48, 08011, Barcelona, Spain</li>
      <li><svg viewBox="0 0 10 10"><text x="0" y="9" font-size="10" font-family="Arimo, sans-serif">@</text></svg>helpdesk@bimsot-example.com</li>
      <li class="contact__web">www.bimsot-example.com</li>
    </ul>
    <div class="rule back-bottom-rule"></div>
  </section>

  <section class="page page--front">
    <div class="rule front-top-rule"></div>
    <p class="doc-kicker">Web Editor Tool</p>
    <h1 class="doc-title">Help Guide</h1>

    <div class="hero" role="img" aria-label="Photograph of a person outdoors at dusk holding a tablet showing a data dashboard"></div>

    <div class="client">
      <div class="client__name">Meridian<br>Harbour</div>
      <span class="client__mark"></span>
    </div>
    <p class="product-name">LDG Actuals Analyser</p>

    <div class="partner">
      <span class="partner__square"></span>
      <span class="partner__name">quorvin</span>
    </div>
    <div class="brand front-brand">
      <span class="brand__square"></span>
      <span class="brand__name">BIMSOT</span>
    </div>
    <div class="rule front-bottom-rule"></div>
    <ol class="page-index">
      <li>1</li><li>2</li><li>3</li><li>4</li><li>5</li><li>6</li><li>7</li><li>8</li><li>9</li>
      <li class="wide">10</li><li class="wide">11</li><li class="wide">12</li><li class="wide">13</li>
    </ol>
  </section>
</body>
</html>
```